Quietude Lantern Habits book cover

Hello!
I need a 5.25x8 VNR paperback cover and ZOB audiobook square cover with the same design. (I might need a Spanish copy as well, but that should just be copy and pasting the translation after the winner is chosen, so don't worry about that for now.)
The title text should be laid out something like this:
A QUICK
WHAT, WHO, WHY, WHERE, HOW & WHEN
-----OF-----
QUIETUDE
LANTERN HABITS
The book should be about 160 pages, for the spine width.
I have attached some concepts/ideas I have for inspiration, but feel free to submit any kinds of ideas you might have. I'm open to your creativity!
~~~~~~~~
Back Sleeve Summary:
Countless studies and anecdotal reports have shown that large doses of psilocybin mushrooms can inspire breakthroughs and mystical experiences or help relieve symptoms of mental health disorders and physical ailments. However, macrodosing psychedelics doesn’t always have a practical application in our day-to-day lives.
Enter microdosing: a method of taking small amounts of psychedelics to invoke a desirable physiological response with minimal undesirable drawbacks. The practice has become more popular in recent years and is proving to be a safe and powerful approach not only to addressing an array of health concerns but also to improving general performance.
Whether you’re looking to taper off pharmaceuticals or simply improve your mood, creativity, sleep, eating habits, physical stamina, or sexual performance, this book will help you learn how microdosing could improve your overall quality of life. The information herein also doesn’t shy away from addressing more controversial topics, such as microdosing in youth or during pregnancy.
This book is intended to provide foundational knowledge of what microdosing is, who is doing it, various motivations for doing so, ideal times and protocols for practice, considerations for where to microdose, and how to go about sourcing and dosing psilocybin mushrooms. It is a carefully researched, beginner-friendly guide that weaves together concise history and research with practical application and integration of microdosing psilocybin.
Author Section (with attached photo):
Dale Pemberton earned a B.S. in Kinesiology from the University of Harwick Vale, and has furthered his studies in the fields of psychedelics, psychology, and trauma healing since 2012. He’s been exploring the benefits of psychedelics within himself for equally as long.
People interested in self help, healing, and microdosing psychedelics.

```html
<!DOCTYPE html>
<html lang="en">
<head>
<meta charset="utf-8">
<title>Quietude Lantern Habits – Book Cover</title>
<link rel="stylesheet" href="https://fonts.googleapis.com/css2?family=Bebas+Neue&family=Montserrat:wght@300;400&display=swap">
<style>
  :root {
    --paper: #ede2b9;
    --ink: #3b3b3b;
    --gold-light: #ecc640;
    --gold: #c99a22;
    --gold-dark: #a27716;
    --rule: #c09a3a;
  }
  html, body { margin: 0; padding: 0; overflow: hidden; }
  body { width: 1200px; height: 873px; background: var(--paper); }
  .cover { position: relative; width: 1200px; height: 873px; background: var(--paper); overflow: hidden; }
  .abs { position: absolute; }
  .back-title { left: 196px; top: 46px; width: 180px; height: 112px; }
  .back-blurb {
    left: 44px; top: 187px; width: 485px; margin: 0;
    font-family: "Montserrat", sans-serif; font-weight: 300;
    font-size: 12.6px; line-height: 16.4px; color: var(--ink);
    text-align: justify; hyphens: auto;
  }
  .back-blurb p { margin: 0; }
  .rule { left: 41px; width: 491px; height: 1.5px; background: var(--rule); }
  .rule-top { top: 420px; }
  .rule-bottom { top: 592px; }
  .author-photo {
    left: 41px; top: 436px; width: 141px; height: 141px;
    background: linear-gradient(160deg, #6a6a6a, #2c2c2c 55%, #8a8a8a);
  }
  .author-bio {
    left: 200px; top: 431px; width: 325px; margin: 0;
    font-family: "Montserrat", sans-serif; font-weight: 300;
    font-size: 12.6px; line-height: 16.4px; color: var(--ink);
    text-align: justify; hyphens: auto;
  }
  .barcode-area { left: 316px; top: 674px; width: 211px; height: 128px; background: #ffffff; }
  .spine { left: 585px; top: 0; width: 30px; height: 873px; }
  .front-photo {
    left: 680px; top: 0; width: 460px; height: 342px;
    background: radial-gradient(ellipse at 50% 35%, #d9b48f 0%, #e6c3a6 35%, #efd2bd 55%, rgba(237,226,185,0) 75%);
  }
  .front-title { left: 686px; top: 450px; width: 460px; height: 290px; }
  .front-author { left: 680px; top: 780px; width: 460px; height: 50px; }
</style>
</head>
<body>
<div class="cover">

  <!-- Back cover -->
  <svg class="abs back-title" viewBox="0 0 180 112" aria-label="A Quick What, Who, Why, Where, How and When of Quietude Lantern Habits">
    <defs>
      <linearGradient id="goldSmall" x1="0" y1="0" x2="0" y2="1">
        <stop offset="0" stop-color="var(--gold-light)"/>
        <stop offset="1" stop-color="var(--gold-dark)"/>
      </linearGradient>
    </defs>
    <text x="90" y="22" text-anchor="middle" font-family="Bebas Neue, sans-serif" font-size="24" fill="var(--ink)">A QUICK</text>
    <text x="6" y="39" font-family="Bebas Neue, sans-serif" font-size="12.5" fill="var(--ink)" textLength="168" lengthAdjust="spacingAndGlyphs">WHAT, WHO, WHY, WHERE, HOW &amp; WHEN</text>
    <line x1="6" y1="47" x2="82" y2="47" stroke="var(--rule)" stroke-width="1"/>
    <line x1="98" y1="47" x2="174" y2="47" stroke="var(--rule)" stroke-width="1"/>
    <text x="90" y="51" text-anchor="middle" font-family="Bebas Neue, sans-serif" font-size="11" fill="var(--ink)">OF</text>
    <text x="6" y="81" font-family="Bebas Neue, sans-serif" font-size="40" fill="url(#goldSmall)" textLength="168" lengthAdjust="spacingAndGlyphs">QUIETUDE</text>
    <text x="6" y="108" font-family="Bebas Neue, sans-serif" font-size="29" fill="url(#goldSmall)" textLength="168" lengthAdjust="spacingAndGlyphs">LANTERN HABITS</text>
  </svg>

  <div class="abs back-blurb">
    <p>Lorem ipsum dolor sit amet, consectetuer adipiscing elit, sed diam nonummy nibh euismod tincidunt ut laoreet dolore magna aliquam erat volutpat. Ut wisi enim ad minim veniam, quis nostrud exerci tation ullamcorper suscipit lobortis nisl ut aliquip ex ea commodo consequat. Duis autem vel eum iriure dolor in hendrerit in vulputate velit esse molestie consequat, vel illum dolore eu feugiat nulla facilisis at vero eros et accumsan et iusto odio dignissim qui blandit praesent luptatum zzril delenit augue duis dolore te feugait nulla facilisi.</p>
    <p>Lorem ipsum dolor sit amet, cons ectetuer adipiscing elit, sed diam nonummy nibh euismod tincidunt ut laoreet dolore magna aliquam erat volutpat. Ut wisi enim ad minim veniam, quis nostrud exerci tation ullamcorper suscipit lobortis nisl ut aliquip ex ea commodo consequat.</p>
    <p>Lorem ipsum dolor sit amet, consectetuer adipiscing elit, sed diam</p>
  </div>

  <div class="abs rule rule-top"></div>
  <div class="abs author-photo" role="img" aria-label="Black and white portrait of author Dale Pemberton seated in an office"></div>
  <p class="abs author-bio">Lorem ipsum dolor sit amet, consectetuer adipiscing elit, sed diam nonummy nibh euismod tincidunt ut laoreet dolore magna aliquam erat volutpat. Ut wisi enim ad minim veniam, quis nostrud exerci tation ullamcorper suscipit lobortis nisl ut aliquip ex ea commodo consequat. Duis autem vel eum iriure dolor in hendrerit in vulputate velit esse molestie consequat, vel illum dolore eu feugiat nulla facilisis at vero eros et</p>
  <div class="abs rule rule-bottom"></div>
  <div class="abs barcode-area"></div>

  <!-- Spine -->
  <svg class="abs spine" viewBox="0 0 30 873" aria-label="Spine: A Quick What, Who, Why, Where, How and When of Quietude Lantern Habits, Dale Pemberton">
    <text transform="translate(9 51) rotate(90)" font-family="Bebas Neue, sans-serif" font-size="17" textLength="662" lengthAdjust="spacingAndGlyphs"><tspan fill="var(--ink)">A QUICK WHAT, WHO, WHY, WHERE, HOW &amp; WHEN OF </tspan><tspan fill="var(--gold)">QUIETUDE LANTERN HABITS</tspan></text>
    <text transform="translate(9 742) rotate(90)" font-family="Bebas Neue, sans-serif" font-size="14" fill="var(--ink)" textLength="93" lengthAdjust="spacingAndGlyphs">DALE PEMBERTON</text>
  </svg>

  <!-- Front cover -->
  <div class="abs front-photo" role="img" aria-label="Photograph of cupped hands holding dried mushrooms surrounded by glowing light streaks"></div>

  <svg class="abs front-title" viewBox="0 0 460 290" aria-label="A Quick What, Who, Why, Where, How and When of Quietude Lantern Habits">
    <defs>
      <linearGradient id="goldLarge" x1="0" y1="0" x2="0" y2="1">
        <stop offset="0" stop-color="var(--gold-light)"/>
        <stop offset="0.55" stop-color="var(--gold)"/>
        <stop offset="1" stop-color="var(--gold-dark)"/>
      </linearGradient>
    </defs>
    <text x="227" y="52" text-anchor="middle" font-family="Bebas Neue, sans-serif" font-size="62" fill="var(--ink)">A QUICK</text>
    <text x="3" y="95" font-family="Bebas Neue, sans-serif" font-size="34" fill="var(--ink)" textLength="451" lengthAdjust="spacingAndGlyphs">WHAT, WHO, WHY, WHERE, HOW &amp; WHEN</text>
    <line x1="3" y1="118.5" x2="205" y2="118.5" stroke="var(--rule)" stroke-width="2"/>
    <line x1="248" y1="118.5" x2="450" y2="118.5" stroke="var(--rule)" stroke-width="2"/>
    <text x="226" y="131" text-anchor="middle" font-family="Bebas Neue, sans-serif" font-size="32" fill="var(--ink)">OF</text>
    <text x="2" y="215" font-family="Bebas Neue, sans-serif" font-size="104" fill="url(#goldLarge)" textLength="451" lengthAdjust="spacingAndGlyphs">QUIETUDE</text>
    <text x="2" y="281" font-family="Bebas Neue, sans-serif" font-size="72" fill="url(#goldLarge)" textLength="451" lengthAdjust="spacingAndGlyphs">LANTERN HABITS</text>
  </svg>

  <svg class="abs front-author" viewBox="0 0 460 50" aria-label="Dale Pemberton">
    <text x="70" y="37" font-family="Bebas Neue, sans-serif" font-size="42" fill="var(--ink)" textLength="320" lengthAdjust="spacing">DALE PEMBERTON</text>
  </svg>

</div>
</body>
</html>
```